Pellmore Heating & Air

I need a business card made for my company. I would like my new logo for Pellmore Heating and Air on the front and my Garage Door on the back.
Front to say -Heating & Air Conditioning , Mini Splits and Heat Pumps, Hydronic In-Floor Heat. Locally Owned and Operated! Licensed, Boned and Insured. Free Estimates on new equipment. 555-201-4837
KVB Back Card, change phone# to 555-318-6024. Remove Commercial and residential and fully sticked vans lines.

```html
<!DOCTYPE html>
<html lang="en">
<head>
<meta charset="utf-8">
<title>Pellmore Heating &amp; Air — Business Card</title>
<link href="https://fonts.googleapis.com/css2?family=Montserrat:wght@400;500;700&display=swap" rel="stylesheet">
<style>
  :root {
    --page-bg: #2a2b30;
    --navy: #243572;
    --navy-deep: #1a2656;
    --navy-ink: #2f4698;
    --navy-text: #8fa2e0;
    --brand-red: #e8352a;
    --brand-blue: #1f4f93;
    --ink: #1d1d22;
    --paper: #ffffff;
  }
  * { box-sizing: border-box; margin: 0; padding: 0; }
  html, body { width: 1200px; height: 900px; overflow: hidden; }
  body {
    background: var(--page-bg);
    font-family: "Montserrat", sans-serif;
    display: flex;
    flex-direction: column;
    align-items: center;
    justify-content: center;
    gap: 40px;
  }
  .card {
    width: 700px;
    height: 400px;
    border-radius: 22px;
    position: relative;
    overflow: hidden;
  }
  .card-front {
    background: linear-gradient(135deg, var(--navy) 0%, var(--navy-deep) 100%);
    display: flex;
    flex-direction: column;
    align-items: center;
    justify-content: center;
    gap: 26px;
    padding: 36px 50px;
  }
  .front-brand {
    font-weight: 700;
    font-size: 46px;
    letter-spacing: 1px;
    color: var(--navy-ink);
    text-transform: uppercase;
    text-align: center;
    line-height: 1.08;
  }
  .front-brand .brand-sub {
    display: block;
    font-size: 30px;
    letter-spacing: 3px;
  }
  .front-details {
    display: grid;
    grid-template-columns: 1fr 1fr;
    column-gap: 40px;
    width: 100%;
  }
  .service-list, .promise-list {
    list-style: none;
    font-size: 14px;
    line-height: 1.7;
    color: var(--navy-text);
  }
  .promise-list { text-align: right; }
  .front-phone {
    font-weight: 700;
    font-size: 22px;
    letter-spacing: 1px;
    color: var(--navy-text);
  }
  .card-back {
    background: var(--paper);
    display: flex;
    align-items: center;
  }
  .back-brand {
    width: 340px;
    padding-left: 50px;
    display: flex;
    align-items: center;
    gap: 14px;
  }
  .brand-mark {
    width: 22px; height: 22px;
    background: var(--brand-blue);
    flex: none;
  }
  .brand-name {
    font-weight: 700;
    font-size: 28px;
    line-height: 1.15;
    color: var(--brand-blue);
    text-transform: uppercase;
  }
  .divider {
    width: 2px;
    height: 220px;
    background: var(--brand-red);
    margin: 0 30px 0 10px;
  }
  .contact { color: var(--ink); }
  .contact-name {
    font-weight: 700;
    font-size: 30px;
    color: var(--brand-red);
  }
  .contact-role { font-size: 15px; margin-bottom: 18px; }
  .contact-address { font-size: 15px; line-height: 1.35; margin-bottom: 14px; }
  .contact-list { list-style: none; }
  .contact-list li {
    display: flex;
    align-items: center;
    gap: 10px;
    font-size: 15px;
    line-height: 1.6;
  }
  .contact-list svg { width: 15px; height: 15px; flex: none; fill: var(--brand-red); }
</style>
</head>
<body>
  <section class="card card-front" aria-label="Card front">
    <h1 class="front-brand">Pellmore<span class="brand-sub">Heating &amp; Air</span></h1>
    <div class="front-details">
      <ul class="service-list">
        <li>Heating &amp; Air Conditioning</li>
        <li>Mini Splits and Heat Pumps</li>
        <li>Hydronic In-Floor Heat</li>
      </ul>
      <ul class="promise-list">
        <li>Locally Owned and Operated!</li>
        <li>Licensed, Bonded and Insured</li>
        <li>Free Estimates on new equipment</li>
      </ul>
    </div>
    <p class="front-phone">555-201-4837</p>
  </section>

  <section class="card card-back" aria-label="Card back">
    <div class="back-brand">
      <span class="brand-mark"></span>
      <span class="brand-name">Kingsvale<br>Garage Door</span>
    </div>
    <div class="divider"></div>
    <div class="contact">
      <h2 class="contact-name">Dana Whitlock</h2>
      <p class="contact-role">owner</p>
      <p class="contact-address">418 Larkin Ave, #112<br>Brookdale, OH 43990</p>
      <ul class="contact-list">
        <li>
          <svg viewBox="0 0 16 16" aria-hidden="true"><path d="M3 1h3l1.5 4-2 1.2a8 8 0 0 0 4.3 4.3L11 8.5l4 1.5v3a2 2 0 0 1-2 2A12 12 0 0 1 1 3a2 2 0 0 1 2-2z"/></svg>
          555-201-4837
        </li>
        <li>
          <svg viewBox="0 0 16 16" aria-hidden="true"><path d="M4 0h8a1 1 0 0 1 1 1v14a1 1 0 0 1-1 1H4a1 1 0 0 1-1-1V1a1 1 0 0 1 1-1zm1 2v10h6V2zm3 11a1 1 0 1 0 0 2 1 1 0 0 0 0-2z"/></svg>
          555-318-6024
        </li>
        <li>
          <svg viewBox="0 0 16 16" aria-hidden="true"><path d="M1 3h14v1L8 9 1 4zm0 3 7 5 7-5v7H1z"/></svg>
          kingsvaledoor@mailbox.com
        </li>
        <li>
          <svg viewBox="0 0 16 16" aria-hidden="true"><path d="M8 0a8 8 0 1 0 0 16A8 8 0 0 0 8 0zm0 1.5c.8 0 1.9 2 2.2 5.5H5.8C6.1 3.5 7.2 1.5 8 1.5zM5.8 9h4.4c-.3 3.5-1.4 5.5-2.2 5.5S6.1 12.5 5.8 9zM1.6 7a6.5 6.5 0 0 1 3-4.8A12 12 0 0 0 4.3 7zm0 2h2.7a12 12 0 0 0 .3 4.8A6.5 6.5 0 0 1 1.6 9zm10.1 0h2.7a6.5 6.5 0 0 1-3 4.8 12 12 0 0 0 .3-4.8zm0-2a12 12 0 0 0-.3-4.8 6.5 6.5 0 0 1 3 4.8z"/></svg>
          www.KingsvaleDoor.com
        </li>
      </ul>
    </div>
  </section>
</body>
</html>
```